Coffee and Plastics

I am looking for a completely new site that shows the products we have. Our current site is www.velmorebrothersroast.com. We are open minded to what designers come up with. Our current site is www.velmorebrothersroast.com. You can you the information from there to start the site. I need these tabs on the main home page. ( Home, Coffee & Tea, Condiments, and Paper and Plastics, and Contact.) You can take photos and info from my Current site. In products page.
I will be uploading info and photo for paper and plastics.
Look and feel
Each slider illustrates characteristics of the customer's brand and the style your logo design should communicate.

```html
<!DOCTYPE html>
<html lang="en">
<head>
<meta charset="utf-8">
<title>Velmore Brothers Roast</title>
<link href="https://fonts.googleapis.com/css2?family=Open+Sans:wght@300;400;600;700&display=swap" rel="stylesheet">
<style>
:root{
  --brand-red:#6b0000;
  --brand-red-bright:#8a0a0a;
  --ink:#000;
  --white:#fff;
  --muted:#d8d0c8;
  --panel:rgba(20,10,5,.55);
  --field:#4a4a4a;
  --wood-dark:#3a1a0c;
  --wood-mid:#6e3416;
  --burlap:#b8946a;
}
*{box-sizing:border-box;margin:0;padding:0}
html,body{width:1200px;height:746px;overflow:hidden;background:var(--ink)}
body{font-family:"Open Sans",Arial,sans-serif;color:var(--white);position:relative}
.topbar{position:absolute;left:0;top:0;width:1200px;height:22px;background:var(--brand-red)}
.topbar .dial{position:absolute;right:210px;top:3px;font-size:13px}
.topbar-rule{position:absolute;left:0;top:22px;width:1200px;height:6px;background:var(--white);border-bottom:1px solid var(--brand-red)}
.header{position:absolute;left:0;top:28px;width:1200px;height:80px;background:linear-gradient(#2a2a2a,#050505)}
.brand-name{position:absolute;left:0;width:1200px;top:22px;text-align:center;font-size:30px;font-weight:300;letter-spacing:1px}
.hero{position:absolute;left:0;top:108px;width:1200px;height:522px;
  background:
    radial-gradient(ellipse 380px 300px at 870px 230px,rgba(70,30,12,.9),transparent 70%),
    radial-gradient(ellipse 420px 360px at 1010px 300px,var(--burlap),transparent 75%),
    linear-gradient(180deg,transparent 60%,rgba(40,15,5,.9) 85%),
    linear-gradient(90deg,var(--wood-dark),var(--wood-mid) 30%,#5a2a12 55%,#4a2210);}
.nav{position:absolute;left:0;top:0;width:1200px;height:27px;background:rgba(0,0,0,.45);display:flex;justify-content:flex-end;padding-right:343px}
.nav a{color:var(--white);text-decoration:none;font-size:12px;line-height:27px;margin-left:28px}
.welcome{position:absolute;left:220px;top:74px;font-size:24px;font-weight:300;line-height:28px}
.intro{position:absolute;left:207px;top:135px;width:256px;height:100px;background:var(--panel);padding:8px 13px;font-size:10.5px;font-weight:300;letter-spacing:-.15px;line-height:17.5px;white-space:nowrap}
.intro-rule{position:absolute;left:207px;top:236px;width:250px;height:3px;background:var(--muted)}
.intro-marker{position:absolute;left:455px;top:229px;width:16px;height:16px;background:var(--brand-red);border:1px solid var(--muted)}
.section-title{position:absolute;left:204px;top:284px;font-size:18px;font-weight:300}
.product-card{position:absolute;top:311px;width:249px;height:124px;background:rgba(25,12,5,.6);display:flex;align-items:center;justify-content:center}
.product-shot{width:120px;height:80px;border-radius:40px}
.shot-tray{background:radial-gradient(circle,#e6c25a,#a07a1e)}
.shot-bowl{width:96px;background:radial-gradient(circle,#fafafa,#cfcfcf);border-radius:48px}
.shot-plate{width:110px;border-radius:8px;background:linear-gradient(#f4f4f4,#cfcfcf)}
.carousel-arrow{position:absolute;top:359px;width:16px;height:28px;overflow:hidden}
.carousel-arrow svg{display:block}
.footer{position:absolute;left:0;top:630px;width:1200px;height:80px;background:linear-gradient(#2c2c2c,#050505)}
.footer h2{position:absolute;top:5px;font-size:14px;font-weight:300}
.field{position:absolute;background:var(--field);font-size:9px;font-style:italic;padding:1px 4px;color:var(--white)}
.submit{position:absolute;left:482px;top:49px;width:35px;height:25px;background:var(--brand-red-bright);font-size:9px;text-align:center;line-height:25px}
.contact{position:absolute;top:27px;font-size:11.5px;line-height:17px;white-space:nowrap}
.contact strong{font-weight:700}
.copyright{position:absolute;left:0;top:710px;width:1200px;height:36px;background:var(--brand-red)}
.copyright p{position:absolute;left:203px;top:10px;font-size:12px}
</style>
</head>
<body>
<div class="topbar"><span class="dial">Dial: 1-800-555-0142</span></div>
<div class="topbar-rule"></div>
<header class="header"><div class="brand-name">Velmore Brothers Roast</div></header>

<main class="hero" role="img" aria-label="Photo of a burlap sack of roasted coffee beans with a metal scoop on a wooden table">
  <nav class="nav">
    <a href="#">Home</a><a href="#">Coffee &amp; Tea</a><a href="#">Condiments</a><a href="#">Paper and Plastics</a><a href="#">Contact</a>
  </nav>
  <h1 class="welcome">Welcome to<br>Velmore Brothers Roast</h1>
  <p class="intro">We are a family-owned and operated business<br>based in Bramford Texas. Since the opening of<br>Velmore Brothers Roast plant in 1995, we have<br>become Texas' premier independently owned<br>coffee packaging company.</p>
  <div class="intro-rule"></div>
  <div class="intro-marker"></div>
  <h2 class="section-title">Other Products</h2>

  <div class="carousel-arrow" style="left:191px"><svg width="16" height="28"><circle cx="16" cy="14" r="14" fill="#fff"/><path d="M6 14l5-4v8z" fill="#000"/></svg></div>
  <div class="product-card" style="left:207px"><div class="product-shot shot-tray" role="img" aria-label="Gold round compartment serving tray"></div></div>
  <div class="product-card" style="left:478px"><div class="product-shot shot-bowl" role="img" aria-label="White plastic bowl"></div></div>
  <div class="product-card" style="left:748px"><div class="product-shot shot-plate" role="img" aria-label="White compartment food tray"></div></div>
  <div class="carousel-arrow" style="left:997px"><svg width="16" height="28"><circle cx="0" cy="14" r="14" fill="#fff"/><path d="M10 14l-5-4v8z" fill="#000"/></svg></div>
</main>

<footer class="footer">
  <h2 style="left:204px">Quick Query</h2>
  <div class="field" style="left:205px;top:29px;width:153px;height:14px">Name:</div>
  <div class="field" style="left:363px;top:29px;width:154px;height:14px">Email:</div>
  <div class="field" style="left:205px;top:49px;width:275px;height:25px">Query:</div>
  <div class="submit">SUBMIT</div>
  <h2 style="left:590px">Contact Details</h2>
  <div class="contact" style="left:591px"><strong>Velmore Brothers</strong><br>Bramford, Texas</div>
  <div class="contact" style="left:713px">Hours: Monday–Friday, 9:00am–5:00pm (CST)<br>Toll Free Phone:&nbsp; 1-800-555-0142 &nbsp; &nbsp; &nbsp;Fax:&nbsp; 903-555-0178</div>
</footer>
<div class="copyright"><p>Copyright © 2014. Velmore Brothers Roast. All Rights Reserved.</p></div>
</body>
</html>
```